BrimTaps.com

Hey guys!

We are looking for an innovative 1 page web design for our PPC network website - http://quickpanelgrab.example/4k7rw2mz8q
We are a PPC social media start up, which works with many social media publishers worldwide.
The design must be clean, flat, trendy, we would like to keep our 1 page design structure, but add your own personal touch-up.

We would like you to make it look like a Million $ company.

Good luck!

Target Market(s)

Big Internet Advertising Companies

Number of Pages Required

1 page

```html
<!DOCTYPE html>
<html lang="en">
<head>
<meta charset="utf-8">
<title>BrimTaps – Publisher Network</title>
<link href="https://fonts.googleapis.com/css2?family=Open+Sans:wght@300;400;600;700&display=swap" rel="stylesheet">
<style>
:root{
  --blue:#3aa6d8;
  --blue-deep:#3b8db3;
  --ink:#333a40;
  --muted:#6b7277;
  --soft:#a7cfe3;
  --band:#f3f3f3;
  --white:#ffffff;
}
*{margin:0;padding:0;box-sizing:border-box}
html,body{width:821px;height:1200px;overflow:hidden;background:var(--white)}
body{font-family:'Open Sans',sans-serif;color:var(--ink);position:relative}
.abs{position:absolute}

/* hero */
.hero{position:absolute;left:0;top:0;width:821px;height:488px;overflow:hidden}
.hero-scene{position:absolute;inset:0;background:
  radial-gradient(ellipse at 70% 45%, #6b7f95 0%, #3e4652 40%, transparent 70%),
  linear-gradient(135deg,#3b3a37 0%,#55524c 35%,#2d3036 70%,#262626 100%)}
.hero-shade{position:absolute;inset:0;background:linear-gradient(90deg,rgba(20,20,22,.55) 0%,rgba(20,20,22,.15) 60%,rgba(20,20,22,0) 100%)}
.brand{left:33px;top:18px;display:flex;align-items:center;gap:8px}
.brand-dot{width:24px;height:24px;border-radius:50%;background:var(--white)}
.brand-name{font-size:21px;font-weight:400;color:var(--white);letter-spacing:.2px}
.nav{left:238px;top:27px;display:flex;gap:17px}
.nav a{font-size:7.6px;font-weight:600;letter-spacing:.9px;color:var(--white);text-decoration:none;text-transform:uppercase}
.btn{display:flex;align-items:center;justify-content:center;border-radius:14px;font-size:7.6px;font-weight:700;letter-spacing:.9px;text-transform:uppercase;text-decoration:none}
.btn-login{left:680px;top:20px;width:50px;height:19px;border:1.5px solid var(--white);color:var(--white);border-radius:10px;font-size:6.8px}
.btn-signup{left:737px;top:20px;width:54px;height:19px;background:var(--blue-deep);color:var(--white);border-radius:10px;font-size:6.8px}
.hero-title{left:30px;top:163px;width:360px;font-size:25px;font-weight:300;line-height:37px;color:var(--white)}
.btn-how{left:30px;top:298px;width:102px;height:28px;border:2px solid var(--white);color:var(--white)}
.btn-join-hero{left:146px;top:299px;width:100px;height:27px;background:var(--blue-deep);color:var(--white)}

/* publisher intro */
.intro-icons{left:318px;top:537px;display:flex;gap:22px}
.intro-title{left:0;top:598px;width:821px;text-align:center;font-size:21.5px;font-weight:300;color:var(--ink)}
.intro-sub{left:0;top:646px;width:821px;text-align:center;font-size:10.5px;color:var(--muted)}
.btn-features{left:308px;top:685px;width:101px;height:27px;border:1.6px solid var(--blue);color:var(--blue)}
.link-team{left:431px;top:694px;font-size:7.6px;font-weight:600;letter-spacing:.9px;color:var(--blue);text-transform:uppercase}

/* benefits band */
.band{position:absolute;left:0;top:764px;width:821px;height:436px;background:var(--band)}
.tab{display:flex;align-items:center;gap:8px;font-size:11px;top:815px}
.tab span{color:var(--soft)}
.tab.active span{color:var(--blue-deep);font-weight:600}
.benefit-title{left:0;top:882px;width:821px;text-align:center;font-size:21.5px;font-weight:300;color:var(--ink)}
.benefit-art{left:99px;top:944px;width:230px;height:198px;border-radius:50%;
  background:radial-gradient(circle at 45% 58%,#4aa6d6 0%,#6fbfe4 38%,#bfe2f3 60%,rgba(243,243,243,0) 72%)}
.benefit-copy{left:420px;top:950px;width:360px;font-size:10.6px;line-height:20px;color:var(--muted)}
.perks{left:427px;top:1006px;list-style:none}
.perks li{display:flex;align-items:center;gap:10px;height:23.5px;font-size:10.6px;color:var(--muted)}
.perks svg{width:11px;height:11px;flex:none}
</style>
</head>
<body>

<header class="hero">
  <div class="hero-scene" role="img" aria-label="Desk photo with a desktop monitor showing the publisher dashboard, a keyboard, a potted plant and a smartphone"></div>
  <div class="hero-shade"></div>

  <div class="abs brand"><span class="brand-dot"></span><span class="brand-name">BrimTaps</span></div>
  <nav class="abs nav">
    <a href="#">Publishers</a><a href="#">Advertisers</a><a href="#">How it works</a><a href="#">Automation</a><a href="#">FAQ</a><a href="#">Contact</a>
  </nav>
  <a class="abs btn btn-login" href="#">Login</a>
  <a class="abs btn btn-signup" href="#">Signup</a>

  <h1 class="abs hero-title">Get Paid To Share High Quality Content That Suits Your Audience</h1>
  <a class="abs btn btn-how" href="#">How it works</a>
  <a class="abs btn btn-join-hero" href="#">Sign up now!</a>
</header>

<section>
  <div class="abs intro-icons">
    <svg width="40" height="34" viewBox="0 0 40 34" fill="none" stroke="#7cc3e4" stroke-width="1.3">
      <rect x="1" y="1" width="38" height="26" rx="1.5"/><rect x="4" y="4" width="32" height="20"/>
      <path d="M16 27v4h8v-4M12 32h16"/>
    </svg>
    <svg width="43" height="34" viewBox="0 0 43 34" fill="none" stroke="#7cc3e4" stroke-width="1.3">
      <rect x="1" y="1" width="41" height="32" rx="1"/><path d="M1 7h41"/>
      <circle cx="4.5" cy="4" r=".8"/><circle cx="7.5" cy="4" r=".8"/><circle cx="10.5" cy="4" r=".8"/>
      <rect x="5" y="12" width="14" height="16"/><path d="M23 13h15M23 18h15M23 23h15M23 28h15"/>
    </svg>
    <svg width="44" height="34" viewBox="0 0 44 34" fill="none" stroke="#7cc3e4" stroke-width="1.3">
      <path d="M3 31l11-13 9 8 18-23"/><circle cx="3" cy="31" r="2"/><circle cx="14" cy="18" r="2"/><circle cx="23" cy="26" r="2"/><circle cx="41" cy="3" r="2"/>
    </svg>
  </div>
  <h2 class="abs intro-title">Become Our Publisher</h2>
  <p class="abs intro-sub">Let Us Show You Why BrimTaps Will Take You Higher</p>
  <a class="abs btn btn-features" href="#">See features</a>
  <a class="abs link-team" href="#">Join our team</a>
</section>

<section class="band"></section>

<div class="abs tab active" style="left:56px">
  <svg width="28" height="26" viewBox="0 0 28 26" fill="none" stroke="#7cc3e4" stroke-width="1.3">
    <path d="M7 2h14v7a7 7 0 0 1-14 0z"/><path d="M7 4H2a5 5 0 0 0 5 7M21 4h5a5 5 0 0 1-5 7"/><path d="M14 16v5M9 24h10"/>
  </svg><span>Premium Benefits</span>
</div>
<div class="abs tab" style="left:255px">
  <svg width="27" height="27" viewBox="0 0 27 27" fill="none" stroke="#c9dfeb" stroke-width="1.3">
    <circle cx="13" cy="14" r="11"/><path d="M13 3v11h11"/><path d="M16 1v10h10a10 10 0 0 0-10-10z"/>
  </svg><span>Detailed Reports</span>
</div>
<div class="abs tab" style="left:441px">
  <svg width="34" height="27" viewBox="0 0 34 27" fill="none" stroke="#c9dfeb" stroke-width="1.3">
    <path d="M14 2a12 9 0 1 0 0 18h2l6 4-1-5a12 9 0 0 0-7-17z"/><path d="M24 11a9 7 0 0 1 8 6 7 7 0 0 1-4 6l1 3-5-3"/>
    <circle cx="9" cy="11" r="1"/><circle cx="14" cy="11" r="1"/><circle cx="19" cy="11" r="1"/>
  </svg><span>Dedicated Support</span>
</div>
<div class="abs tab" style="left:654px">
  <svg width="27" height="27" viewBox="0 0 27 27" fill="none" stroke="#c9dfeb" stroke-width="1.3">
    <circle cx="13.5" cy="13.5" r="12"/><ellipse cx="13.5" cy="13.5" rx="5.5" ry="12"/><path d="M1.5 13.5h24M3.5 7h20M3.5 20h20M13.5 1.5v24"/>
  </svg><span>Social Power</span>
</div>

<h2 class="abs benefit-title">Active And Consistent Publishers - BrimTaps Wants To Reward You!</h2>
<div class="abs benefit-art" role="img" aria-label="Illustration of a rocket orbiting the globe among small stars"></div>

<p class="abs benefit-copy">We know what your real value is, and you deserve the best. Therefore, BrimTaps provide you with the best terms and incentives in the industry</p>
<ul class="abs perks">
  <li><svg viewBox="0 0 11 11" fill="none" stroke="#bbb"><rect x=".5" y=".5" width="10" height="10"/><path d="M.5 4h10M.5 7.5h10M4 .5v10M7.5 .5v10"/></svg>Weekly Payments</li>
  <li><svg viewBox="0 0 11 11" fill="none" stroke="#bbb"><path d="M1 10.5h9.5M2 10V6h2v4M5 10V3h2v7M8 10V5h2v5"/></svg>The Highest CPC In The Industry</li>
  <li><svg viewBox="0 0 11 11" fill="none" stroke="#bbb"><path d="M3 1h5v3a2.5 2.5 0 0 1-5 0zM3 2H1a2 2 0 0 0 2 3M8 2h2a2 2 0 0 1-2 3M5.5 6.5v2.5M3.5 10h4"/></svg>Get Access To The Most Exclusive &amp; Premium Media Campaigns</li>
  <li><svg viewBox="0 0 11 11" fill="none" stroke="#bbb"><circle cx="5.5" cy="5.5" r="4.8"/><path d="M2 9l7-7"/></svg>Advanced Tracking &amp; Detailed Reports Platform</li>
  <li><svg viewBox="0 0 11 11" fill="none" stroke="#bbb"><circle cx="4" cy="7" r="3"/><circle cx="8" cy="3" r="2.3"/></svg>Automate Your Social Pages Monetization With Just a Few Clicks</li>
</ul>

</body>
</html>
```